Flyer-Design für betriebliche Gesundheitsvorsorge
Zielgruppe
'Werk im Schwung' soll Unternehmen die Möglichkeit bieten unsere Dienste im Sinne der Gesundheitsvorsorge für ihre Mitarbeiter in Anspruch zu nehmen. Dies beinhaltet Massagen am Arbeitsplatz (in separaten Räumlichkeiten), Arbeitsplatzberatung bezgl. Ergonomie, Workshops zu kurzen Übungen die in den Arbeitsalltag integriert werden können, Verdeutlichung der Eigenverantwortung für einen gesunden Körper, ....
Aufgabenstellung
Die Werbekarte sollte in DIN Lang format sein.

```html
<!DOCTYPE html>
<html lang="de">
<head>
<meta charset="utf-8">
<title>Werk im Schwung – Flyer</title>
<link rel="stylesheet" href="https://fonts.googleapis.com/css2?family=Ubuntu:wght@300;400;500&display=swap">
<style>
  :root {
    --teal: #3bbab3;
    --teal-dark: #2fa59f;
    --grey: #58595b;
    --mat: #e2e2e2;
    --white: #ffffff;
    --photo-light: #f1f2f2;
    --photo-mid: #d9dcdc;
  }
  * { box-sizing: border-box; margin: 0; padding: 0; }
  html, body {
    width: 1200px; height: 735px; overflow: hidden;
    background: var(--mat);
    font-family: "Ubuntu", sans-serif;
  }
  .flyer {
    position: absolute; left: 112px; top: 123px;
    width: 976px; height: 488px;
    background: var(--white);
    overflow: hidden;
  }
  .flyer-shapes { position: absolute; inset: 0; }
  .brand {
    position: absolute; left: 22px; top: 20px;
    display: flex; align-items: center; height: 100px;
  }
  .brand-mark {
    width: 70px; height: 70px; border-radius: 50%;
    background: var(--teal); margin-right: 28px;
  }
  .brand-divider {
    width: 1px; height: 104px; background: var(--grey);
    margin-right: 12px;
  }
  .brand-text { display: flex; flex-direction: column; }
  .brand-name {
    font-size: 44px; font-weight: 500; color: var(--teal);
    line-height: 1; letter-spacing: 0.5px;
  }
  .brand-tagline {
    margin-top: 10px; font-size: 12px; font-weight: 300;
    color: var(--grey); letter-spacing: 1.4px;
  }
  .claim {
    position: absolute; left: 18px; top: 122px;
    width: 414px; height: 28px; border-radius: 14px;
    background: var(--teal); color: var(--white);
    font-size: 14px; line-height: 28px; padding-left: 22px;
  }
  .services {
    position: absolute; left: 18px; top: 158px; width: 414px;
    text-align: center; color: var(--teal);
    font-size: 22px; font-weight: 300; line-height: 28px;
    letter-spacing: 1.3px;
  }
  .contact {
    position: absolute; left: 608px; top: 41px;
    width: 368px; height: 66px;
    background: var(--teal);
    border-radius: 33px 0 0 33px;
    color: var(--white); text-align: right;
    padding-right: 22px;
  }
  .contact-row { display: flex; justify-content: flex-end; align-items: center; }
  .contact-phone { font-size: 28px; font-weight: 300; height: 38px; margin-top: 2px; }
  .contact-mail { font-size: 17px; height: 22px; }
  .contact-icon {
    width: 22px; height: 22px; border-radius: 50%;
    background: var(--white); margin-left: 9px;
    display: flex; align-items: center; justify-content: center;
  }
  .web {
    position: absolute; left: 178px; top: 450px;
    font-size: 18px; color: var(--white); letter-spacing: 0.3px;
  }
  .signoff {
    position: absolute; right: 20px; top: 420px;
    text-align: right; color: var(--white);
  }
  .signoff-title { font-size: 25px; line-height: 28px; }
  .signoff-sub { font-size: 18px; line-height: 24px; }
</style>
</head>
<body>
<main class="flyer">
  <svg class="flyer-shapes" width="976" height="488" viewBox="0 0 976 488">
    <defs>
      <linearGradient id="photoTone" x1="0" y1="0" x2="1" y2="1">
        <stop offset="0" stop-color="var(--photo-light)"/>
        <stop offset="1" stop-color="var(--photo-mid)"/>
      </linearGradient>
      <linearGradient id="officeTone" x1="0" y1="0" x2="0" y2="1">
        <stop offset="0" stop-color="#c9cfd4"/>
        <stop offset="1" stop-color="#9fb1c8"/>
      </linearGradient>
      <linearGradient id="warehouseTone" x1="0" y1="0" x2="0" y2="1">
        <stop offset="0" stop-color="#6b5f58"/>
        <stop offset="1" stop-color="#a08f72"/>
      </linearGradient>
    </defs>
    <rect x="440" y="62" width="520" height="380" fill="url(#photoTone)" role="img"
          aria-label="Foto: Therapeutin neben einem weißen Kleinwagen mit Firmenbeschriftung und einer zusammengeklappten Massageliege"/>
    <path class="wave" fill="var(--teal)"
          d="M0 488 V450 C60 390 140 355 260 352 C420 350 540 420 640 418 C780 414 900 370 976 323 V488 Z"/>
    <circle cx="105" cy="384" r="87" fill="url(#warehouseTone)" role="img"
            aria-label="Foto: Lagerarbeiter mit Rückenschmerzen"/>
    <circle cx="280" cy="354" r="75" fill="url(#officeTone)" role="img"
            aria-label="Foto: Büroangestellte hält sich den verspannten Nacken"/>
    <circle cx="441" cy="385" r="63" fill="url(#officeTone)" role="img"
            aria-label="Foto: Frau mit Nackenschmerzen am Arbeitsplatz"/>
  </svg>

  <header class="brand">
    <div class="brand-mark"></div>
    <div class="brand-divider"></div>
    <div class="brand-text">
      <span class="brand-name">Werk im Schwung</span>
      <span class="brand-tagline">Gesundheitsvorsorge am Arbeitsplatz</span>
    </div>
  </header>

  <p class="claim">Präventive Intervention bei haltungsbedingten Schmerzen</p>

  <p class="services">
    Heilmassage - Sportmassage<br>
    Bindegewebemassage - Schröpfen<br>
    Aromatherapie - Kinesio Taping
  </p>

  <address class="contact">
    <div class="contact-row contact-phone">
      <span>+43 (0) 660 123 4567</span>
      <span class="contact-icon">
        <svg width="14" height="14" viewBox="0 0 24 24" fill="none" stroke="var(--teal)" stroke-width="2.2" stroke-linejoin="round">
          <path d="M5 3h4l2 5-2.5 1.5a11 11 0 0 0 6 6L16 13l5 2v4a2 2 0 0 1-2 2A16 16 0 0 1 3 5a2 2 0 0 1 2-2z"/>
        </svg>
      </span>
    </div>
    <div class="contact-row contact-mail">
      <span>hallo@werkimschwung.com</span>
      <span class="contact-icon">
        <svg width="13" height="13" viewBox="0 0 24 24" fill="none" stroke="var(--teal)" stroke-width="2.2" stroke-linejoin="round">
          <rect x="3" y="5" width="18" height="14" rx="1"/>
          <path d="M3 6l9 7 9-7"/>
        </svg>
      </span>
    </div>
  </address>

  <p class="web">www.werkimschwung.com</p>

  <footer class="signoff">
    <p class="signoff-title">WERK IM SCHWUNG</p>
    <p class="signoff-sub">Gesundheitsvorsorge an Ihrem Arbeitsplatz</p>
  </footer>
</main>
</body>
</html>
```